Business Card for Kinesiologist Practitioner

I need a logo and business card designing for a Kinesiologist Practitioner. I would like the card to be double sided. The look and feel of the logo and graphics should depict natural healing and well being. I would like a modern, fresh and contemporary design with a professional style. I have attached some logos and business cards that I liek from other natural health practitioners. I have also attached some logos that I like and a mock up of the business card style. Please however use your own creative input to change any element as you feel appropriate.

I have used the strap line "Quiet Renewal" which I would like underneath the logo. For the logo I like natural objects and possibly with 3 elements in the design as the course I have studied follows a "Open Arc " healing concept (mind, body, soul). Maybe a tree or flower with 3 elements and a representation or suggestion of the human body somehow. You will see from the logos i have uploaded

Industry/Entity Type

Business

Contact Information for Business Card

Please see the mock up attached.

Font styles to use
Serif
Sans Serif

Colors
faa54b
acd036
fbee3d
85cae6

Requirements
Must have
• Note the colours are just suggested colours. Please us your own creative licence.

```html
<!DOCTYPE html>
<html lang="en">
<head>
<meta charset="utf-8">
<title>Quiet Renewal – Business Card</title>
<link href="https://fonts.googleapis.com/css2?family=Comfortaa:wght@300;400;700&display=swap" rel="stylesheet">
<style>
  :root {
    --stage: #e9e6e1;
    --card-black: #0b0b0b;
    --card-black-2: #262626;
    --leaf-green: #9ccc3a;
    --leaf-green-light: #b6dc5c;
    --leaf-green-dark: #6fa82a;
    --accent-orange: #f6b23f;
    --text-light: #e8e8e8;
    --text-muted: #a9a9a9;
  }
  * { box-sizing: border-box; margin: 0; padding: 0; }
  html, body { width: 1200px; height: 1023px; overflow: hidden; }
  body {
    background: var(--stage);
    font-family: "Comfortaa", sans-serif;
    position: relative;
  }
  .card {
    position: absolute;
    width: 540px;
    height: 309px;
    border-radius: 22px;
    overflow: hidden;
    box-shadow: 0 10px 28px rgba(0,0,0,.22);
  }
  .card-front {
    left: 40px; top: 357px;
    background: linear-gradient(160deg, var(--card-black-2), var(--card-black) 55%);
  }
  .card-back {
    left: 620px; top: 357px;
    background: radial-gradient(circle at 55% 40%, var(--leaf-green-light), var(--leaf-green) 55%, var(--leaf-green-dark));
    display: flex; align-items: center; justify-content: center; gap: 16px;
  }
  .front-swoosh { position: absolute; inset: 0; }
  .brand-title {
    position: absolute; right: 32px; top: 26px;
    font-size: 34px; font-weight: 300; color: var(--accent-orange);
    letter-spacing: .5px; line-height: 1.2;
  }
  .identity {
    position: absolute; right: 32px; top: 82px; text-align: right;
  }
  .person-name { font-size: 19px; font-weight: 700; color: var(--accent-orange); }
  .person-cred { font-size: 13px; color: var(--text-light); font-weight: 400; }
  .person-role { font-size: 11px; color: var(--text-muted); margin-top: 4px; }
  .divider {
    position: absolute; right: 32px; top: 132px;
    width: 230px; height: 1.5px; background: var(--accent-orange);
  }
  .contacts {
    position: absolute; right: 32px; top: 144px;
    list-style: none; text-align: right;
  }
  .contacts li {
    display: flex; align-items: center; justify-content: flex-end; gap: 8px;
    font-size: 12px; color: var(--text-light); margin-bottom: 8px;
  }
  .contact-icon {
    width: 16px; height: 16px; border-radius: 50%;
    background: var(--accent-orange);
    display: inline-flex; align-items: center; justify-content: center;
  }
  .front-mark {
    position: absolute; left: 40px; top: 150px;
    display: flex; align-items: center; gap: 10px;
  }
  .mark-dot { width: 18px; height: 18px; border-radius: 50%; background: var(--accent-orange); }
  .mark-name { font-size: 20px; font-weight: 400; color: var(--leaf-green-light); }
  .back-dot { width: 26px; height: 26px; border-radius: 50%; background: #ffffff; }
  .back-name { font-size: 32px; font-weight: 300; color: #ffffff; }
</style>
</head>
<body>
  <section class="card card-front" aria-label="Business card front">
    <svg class="front-swoosh" viewBox="0 0 540 309" preserveAspectRatio="none" aria-hidden="true">
      <path d="M540 212 C 480 260, 380 285, 220 309 L540 309 Z" fill="var(--leaf-green)"/>
      <path d="M540 212 C 480 260, 380 285, 220 309" fill="none" stroke="var(--leaf-green-light)" stroke-width="3"/>
    </svg>
    <h1 class="brand-title">Quiet Renewal</h1>
    <div class="identity">
      <p><span class="person-name">Mara Lindell</span> <span class="person-cred">Dip. Cert.</span></p>
      <p class="person-role">Kinesiologist</p>
    </div>
    <div class="divider"></div>
    <ul class="contacts">
      <li>0400 123 456
        <span class="contact-icon"><svg width="9" height="9" viewBox="0 0 24 24"><path d="M6.6 10.8a15 15 0 0 0 6.6 6.6l2.2-2.2a1 1 0 0 1 1-.25 11 11 0 0 0 3.6.6 1 1 0 0 1 1 1V20a1 1 0 0 1-1 1A17 17 0 0 1 3 4a1 1 0 0 1 1-1h3.5a1 1 0 0 1 1 1c0 1.25.2 2.45.6 3.6a1 1 0 0 1-.25 1z" fill="#111"/></svg></span>
      </li>
      <li>maralindell@mail.com
        <span class="contact-icon"><svg width="9" height="9" viewBox="0 0 24 24"><rect x="2" y="5" width="20" height="14" rx="2" fill="#111"/><path d="M3 6l9 7 9-7" stroke="#f6b23f" stroke-width="2" fill="none"/></svg></span>
      </li>
    </ul>
    <div class="front-mark">
      <span class="mark-dot"></span>
      <span class="mark-name">Quiet Renewal</span>
    </div>
  </section>

  <section class="card card-back" aria-label="Business card back">
    <span class="back-dot"></span>
    <span class="back-name">Quiet Renewal</span>
  </section>
</body>
</html>
```